Business Card Design - Furniture Retail

Open to both Single or double sided design

We are launching a online ecommerce store that sells Scandinavian/Danish style of furniture in Australia.

We aspire to provide stylish but classic and designers' selection of furniture to the Australia public at affordable price. For the style of the furniture we are selling, please see the following links:

https://www.boxlyshare.com/sh/qrk7vz2mwpl04tn/BBXTpeLr3h52Kd7nWqYzRsGmu?dl=0

The style of the design we are looking for is clean, simple that look Scandinavian/Danish but yet it is timeless classic.

Aspiring Design
http://www.hallwick.com
http://brenlowe.com.au/
http://kolvo.furniture/
http://www.tipo.com/
Updates

Please display the card on normal angle for both front and back instead of funny angle. Please keep it display when displaying the design of the business cards so that we can focus on the designs rather than being confused by the unnecessary stuffs like the hands or background

I think there is already enough curve line on the logo itself so anything extra of the curve on the business card would be really unnecessary. Please avoid using any of the extra curve line on the business card, other than the logo itself. Thanks

Regular card and give them a matt celloglaze to create texture on card that makes it looked luxury and expensive.

Please display design on normal angle! Please only use white colour in the background (not the business card but the referring to the submission) rather than anything fancy so that we can focus on the design.

Target Market(s)

High end market consumers who are financially capable and who has good taste and appreciate good design

aged between 28 - 45 white collars professional/businessmen who live in metropolitan areas

Industry/Entity Type

Business

Font styles to use
Serif
Sans Serif

Requirements
Must have
• Regular card and give them a matt celloglaze to create texture on card that makes it looked luxury and expensive.

Please use the logo from the uploaded files

Company Name: Miles Orveda
Name: Peter Holm
Phone: +614 27 505 316
Website: www.milesorveda.com.au
Email: peter@milesorveda.com.au
Nice to have
• Colour is not limited to black and white
Should not have
• The concept photos of the furniture should NOT be used in the FRONT page of the business card.

```html
<!DOCTYPE html>
<html lang="en">
<head>
<meta charset="utf-8">
<title>Miles Orveda — Business Card</title>
<link rel="stylesheet" href="https://fonts.googleapis.com/css2?family=Noto+Serif:wght@400&family=Arimo:wght@400&display=swap">
<style>
  :root {
    --page-bg: #ffffff;
    --card-dark: #0b0b0b;
    --card-dark-grain: #1a1a1a;
    --card-light: #ffffff;
    --ink: #111111;
    --ink-soft: #222222;
    --paper-white: #f4f4f4;
    --card-edge: #2a2a2a;
  }
  html, body {
    margin: 0;
    padding: 0;
    width: 1200px;
    height: 1200px;
    overflow: hidden;
    background: var(--page-bg);
  }
  .presentation {
    position: relative;
    width: 1200px;
    height: 1200px;
  }
  .card {
    position: absolute;
    left: 343px;
    width: 508px;
    height: 290px;
    box-sizing: border-box;
  }
  .card--front {
    top: 270px;
    background: var(--card-dark);
  }
  .card__texture {
    position: absolute;
    inset: 0;
    background:
      repeating-linear-gradient(178deg, transparent 0 22px, rgba(255,255,255,0.025) 22px 24px, transparent 24px 41px),
      linear-gradient(180deg, var(--card-dark-grain) 0%, var(--card-dark) 45%, var(--card-dark-grain) 100%);
  }
  .card--back {
    top: 632px;
    background: var(--card-light);
    border: 1px solid var(--card-edge);
  }
  .wordmark {
    position: absolute;
    left: 0;
    right: 0;
    text-align: center;
    font-family: "Noto Serif", Georgia, serif;
    font-weight: 400;
    text-transform: uppercase;
    letter-spacing: 0.06em;
    white-space: nowrap;
    line-height: 1;
  }
  .card--front .wordmark {
    top: 134px;
    font-size: 22px;
    color: var(--paper-white);
  }
  .card--back .wordmark {
    top: 78px;
    font-size: 22px;
    color: var(--ink);
  }
  .contact {
    position: absolute;
    left: 0;
    right: 0;
    text-align: center;
    color: var(--ink-soft);
  }
  .contact__name {
    top: 150px;
    font-family: "Noto Serif", Georgia, serif;
    font-size: 19px;
    line-height: 1;
  }
  .contact__phone {
    top: 196px;
    font-family: "Arimo", Arial, sans-serif;
    font-size: 13px;
    line-height: 1;
  }
  .contact__links {
    top: 225px;
    font-family: "Arimo", Arial, sans-serif;
    font-size: 10px;
    line-height: 11px;
  }
  .contact__links span {
    display: block;
  }
</style>
</head>
<body>
  <main class="presentation">
    <section class="card card--front">
      <div class="card__texture" role="img" aria-label="Dark black wood grain card finish"></div>
      <div class="wordmark">Miles Orveda</div>
    </section>

    <section class="card card--back">
      <div class="wordmark">Miles Orveda</div>
      <div class="contact contact__name">Peter Holm</div>
      <div class="contact contact__phone">+614 27 505 316</div>
      <div class="contact contact__links">
        <span>www.milesorveda.com.au</span>
        <span>peter@milesorveda.com.au</span>
      </div>
    </section>
  </main>
</body>
</html>
```